website homepage design sample for tallowreach.com.au

Hello, I am looking to update my website to be simpler and more modern and to include space for my upcoming online courses. Please review my website tallowreach.com.au for an idea of me as a male psychologist, as well as my services. I would like it to be NOT too feminine. Target market is Men and women interested in couselling, life coaching, and online courses about relationships. Id like to keep the beach theme if possible but I am open to better ideas. thank you!

please see tallowreach.com.au for my current wordpress website.

Target Market(s)

Men and Women

Industry/Entity Type

psychology

Number of Pages Required

1 page

Requirements
Must have
• An "Online Training" Menu that includes links to "Map your Bearings" , "Lantern and Compass Workbook," "Quiet Harbour Program" "Where Did All the Summers Go" "Tending the Willow Garden"

```html
<!DOCTYPE html>
<html lang="en">
<head>
<meta charset="utf-8">
<title>Tallowreach – Psychology Solutions + Your Choices</title>
<link href="https://fonts.googleapis.com/css2?family=Gelasio:wght@400;500&family=Poppins:wght@400;500&display=swap" rel="stylesheet">
<style>
:root{
  --teal:#0b97b9;
  --teal-dark:#0a86a5;
  --ice:#dff1f6;
  --panel:#f6f6f6;
  --ink:#1f2328;
  --body:#5b6169;
  --rule:#d9dde1;
  --white:#ffffff;
}
*{box-sizing:border-box;margin:0;padding:0}
html,body{width:1200px;height:5177px;overflow:hidden;background:var(--white)}
body{position:relative;font-family:"Poppins",sans-serif;color:var(--body);font-size:10px;line-height:1.85}
.abs{position:absolute}
h1,h2,h3,h4,.serif{font-family:"Gelasio",serif;font-weight:400;color:var(--ink)}
a{color:inherit}
.btn{position:absolute;display:flex;align-items:center;justify-content:center;background:var(--teal);color:var(--white);font-size:10px;font-weight:500;text-decoration:none}
.btn.outline{background:var(--white);border:1.5px solid var(--teal);color:var(--teal)}
.ph{position:absolute}

/* header */
.site-header{position:absolute;left:0;top:0;width:1200px;height:68px;background:var(--white)}
.brand{position:absolute;left:52px;top:22px;display:flex;align-items:center;gap:8px;font-family:"Poppins",sans-serif;font-weight:500;font-size:13px;color:var(--teal);letter-spacing:.5px}
.brand i{width:18px;height:18px;border-radius:50%;background:var(--teal);display:block}
.nav{position:absolute;right:46px;top:26px;display:flex;gap:28px;list-style:none;font-size:9.5px;color:var(--body)}
.nav li{position:relative}
.nav li.active{color:var(--teal)}
.nav .caret::after{content:"⌄";margin-left:4px;font-size:9px}
.submenu{display:none;position:absolute;top:20px;left:0;width:230px;background:var(--white);list-style:none;padding:10px 14px;box-shadow:0 4px 14px rgba(0,0,0,.08)}
.nav li:hover .submenu{display:block}

/* hero */
.hero{position:absolute;left:0;top:68px;width:1200px;height:600px;background:var(--ice)}
.hero h1{position:absolute;left:164px;top:166px;font-size:68px;line-height:1}
.hero .tag{position:absolute;left:166px;top:250px;font-family:"Gelasio",serif;font-size:19px;color:var(--teal)}
.hero p{position:absolute;left:166px;top:292px;width:350px;color:var(--ink);font-size:9.5px}

/* about */
.about{position:absolute;left:150px;top:880px;width:900px;height:392px;background:var(--panel);border-top:2px solid var(--teal);text-align:center}
.avatar{position:absolute;left:512px;top:792px;width:176px;height:176px;border-radius:50%;background:linear-gradient(160deg,#b9a08e,#6f5a4e);border:3px solid var(--white)}
.about h2{position:absolute;left:0;right:0;top:132px;font-size:19px}
.about p{position:absolute;left:110px;right:110px;top:186px;font-size:9px}

/* slider */
.slider{position:absolute;left:0;top:1446px;width:1200px;height:500px;display:flex}
.slide{position:relative;width:300px;height:500px}
.slide span{position:absolute;left:0;right:0;bottom:56px;text-align:center;font-family:"Gelasio",serif;font-size:18px;color:var(--white)}
.arrow{position:absolute;top:1677px;width:36px;height:36px;background:var(--white);display:flex;align-items:center;justify-content:center;color:var(--ink);font-size:14px}

/* telehealth */
.tele{position:absolute;left:150px;top:2145px;width:900px;height:505px;background:var(--teal)}
.tele .card{position:absolute;left:122px;top:101px;width:656px;height:302px;background:var(--white);text-align:center}
.tele h2{margin-top:64px;font-size:30px;line-height:1.3}
.tele .rebate{font-family:"Gelasio",serif;font-size:20px;color:var(--teal);margin-top:14px}
.tele .values{font-size:9px;margin-top:18px}

/* intro */
.intro h2{position:absolute;left:150px;top:2800px;font-size:31px}
.intro .sub{position:absolute;left:152px;top:2858px;font-family:"Gelasio",serif;font-size:19px;color:var(--teal)}
.intro p{position:absolute;left:150px;width:590px;font-size:9px}
.checks{position:absolute;left:150px;top:3036px;width:330px;list-style:none;columns:2;column-gap:20px;font-size:9.5px}
.checks li{display:flex;align-items:center;gap:8px;height:28px;break-inside:avoid}
.tick{width:13px;height:13px;flex:none}

/* self worth */
.worth{position:absolute;left:150px;top:3385px;width:900px;height:525px;background:var(--ice)}
.worth h2{position:absolute;left:383px;top:84px;font-size:32px}
.worth p{position:absolute;left:383px;top:140px;width:462px;font-size:9px;line-height:1.95;color:var(--ink)}
.worth p u{color:var(--ink)}

/* objectives */
.objectives h2{position:absolute;left:0;right:0;top:4018px;text-align:center;font-size:30px}
.obj{position:absolute;top:4108px;width:285px}
.obj .img{height:290px}
.obj .cap{position:relative;width:215px;margin-top:-40px;padding:40px 0 0;background:var(--white);font-size:9px}

/* footer */
.footer-rule{position:absolute;left:150px;width:900px;height:1px;background:var(--rule)}
.fcol{position:absolute;top:4680px;width:220px}
.fcol h4{font-size:19px;margin-bottom:18px}
.fcol ul{list-style:none;font-size:9px}
.fcol li{display:flex;align-items:center;gap:10px;height:27px}
.foot-brand{position:absolute;left:0;right:0;top:4982px;display:flex;justify-content:center;align-items:center;gap:8px;font-weight:500;font-size:13px;color:var(--teal);letter-spacing:.5px}
.foot-brand i{width:18px;height:18px;border-radius:50%;background:var(--teal);display:block}
.legal{position:absolute;left:0;right:0;top:5042px;text-align:center;font-size:8.5px}
.copy{position:absolute;left:0;right:0;top:5080px;text-align:center;font-size:8.5px}
</style>
</head>
<body>
<svg width="0" height="0" style="position:absolute">
  <symbol id="tick" viewBox="0 0 14 14"><circle cx="7" cy="7" r="6" fill="none" stroke="#0b97b9" stroke-width="1.2"/><path d="M4 7.2l2 2 4-4.2" fill="none" stroke="#0b97b9" stroke-width="1.3"/></symbol>
</svg>

<header class="site-header">
  <div class="brand"><i></i>TALLOWREACH</div>
  <ul class="nav">
    <li class="active">Home</li>
    <li>About</li>
    <li class="caret">Services &amp; Fees</li>
    <li class="caret">Online Training
      <ul class="submenu">
        <li>Map your Bearings</li>
        <li>Lantern and Compass Workbook</li>
        <li>Quiet Harbour Program</li>
        <li>Where Did All the Summers Go</li>
        <li>Tending the Willow Garden</li>
      </ul>
    </li>
    <li>Blog</li>
    <li>Contact</li>
  </ul>
</header>

<section class="hero">
  <h1>Tallowreach</h1>
  <div class="tag">Psychology Solutions + Your Choices</div>
  <p>At Tallowreach, we are focused on your mental wellness. Tallowreach is open to anyone looking for an Online or <u>Gold Coast Psychologist</u> to help them overcome barriers and find fulfilment in their lives. We also offer do it yourself educational programs.</p>
  <a class="btn" style="left:166px;top:398px;width:150px;height:36px">Book Appointment</a>
  <div class="ph" role="img" aria-label="Line illustration of overlapping head profiles in teal" style="left:665px;top:104px;width:360px;height:400px;background:radial-gradient(ellipse at 55% 45%,#a9dbe7 0%,#cfeaf1 55%,rgba(223,241,246,0) 75%)"></div>
</section>

<section class="about">
  <h2>An Experienced Gold Coast Psychologist, Also Available Online.</h2>
  <p>Unfortunately, we all go through periods of crisis in our lives. When we find ourselves struggling for an extended period, we can use a bit of help to work through barriers that stand in our way. Counselling or psychotherapy can help. Contact Daniel, your Gold Coast Psychologist.<br>Daniel has 15 years experience in providing counselling and psychotherapy to people from all walks of life. Daniel understands the different challenges that people of all backgrounds face in coming to seek help and has a variety of treatments to help.</p>
  <a class="btn outline" style="left:391px;top:296px;width:116px;height:36px">Online Help</a>
</section>
<div class="avatar" role="img" aria-label="Portrait photo of the psychologist"></div>

<section class="slider">
  <div class="slide" role="img" aria-label="Photo of a person writing notes during a counselling session" style="background:linear-gradient(160deg,#4a3d38,#1f1a18)"><span>Psychological Counselling</span></div>
  <div class="slide" role="img" aria-label="Photo of a smiling woman hugging herself" style="background:linear-gradient(160deg,#a7d3dc,#e59fb2)"><span>Self Esteem Course Only $47</span></div>
  <div class="slide" role="img" aria-label="Photo of the psychologist in low light" style="background:linear-gradient(160deg,#3a2e28,#0f0c0b)"><span>About Daniel</span></div>
  <div class="slide" role="img" aria-label="Photo of a hand placing a jigsaw piece" style="background:linear-gradient(160deg,#c9a99a,#7aa3c2)"><span>View Our Services &amp; Fees</span></div>
</section>
<div class="arrow" style="left:60px">‹</div>
<div class="arrow" style="left:1104px">›</div>

<section class="tele">
  <div class="card">
    <h2>Gold Coast Psychologist<br>Also Offering Australia-Wide Telehealth</h2>
    <div class="rebate">Health Fund Rebates Available</div>
    <div class="values">Experienced – Caring – Understanding – Effective – Affordable</div>
  </div>
</section>

<section class="intro">
  <h2>Tallowreach By Daniel Hartley</h2>
  <div class="sub">Psychologist Gold Coast</div>
  <p style="top:2914px">Congratulations on taking the first step to overcoming your barriers and being who you want to be. At Tallowreach, we are focused on your mental wellness. Tallowreach is open to anyone looking for a Gold Coast Psychologist or online therapist to help them overcome barriers and find fulfilment in their lives. We also offer online programs.</p>
  <p style="top:2988px">Daniel, your Gold Coast Psychologist, can help you through a variety of challenges:</p>
  <ul class="checks">
    <li><svg class="tick"><use href="#tick"/></svg>Depression</li>
    <li><svg class="tick"><use href="#tick"/></svg>Relationship problems</li>
    <li><svg class="tick"><use href="#tick"/></svg>Personal development</li>
    <li><svg class="tick"><use href="#tick"/></svg>Trauma and EMDR</li>
    <li><svg class="tick"><use href="#tick"/></svg>Anxiety</li>
    <li><svg class="tick"><use href="#tick"/></svg>ADHD</li>
    <li><svg class="tick"><use href="#tick"/></svg>Anger management</li>
    <li><svg class="tick"><use href="#tick"/></svg>Life Coaching</li>
  </ul>
  <a class="btn" style="left:151px;top:3172px;width:120px;height:36px">Book Online</a>
  <div class="ph" role="img" aria-label="Illustration of blue steps rising into an upward arrow" style="left:560px;top:2780px;width:480px;height:470px;background:radial-gradient(ellipse at 60% 50%,#5fa6ea 0%,#b9dcf6 45%,rgba(255,255,255,0) 72%)"></div>
</section>

<section class="worth">
  <h2>Finding Self Worth</h2>
  <p>Wondering where to start? Watch our free <u>Self Worth Webinar</u><br>Wondering how your self esteem stacks up? Take our <u>Map your Bearings</u> quiz.<br>Interested in a what psychotherapy can offer but not quite ready? Try our <u>Self Esteem Course</u><br>Your Online or Gold Coast Psychologist should not only be about moving away from what makes you sad, but moving towards what makes you happy, resilient, engaged and fulfilled. At Tallowreach, Daniel combines evidence-based treatment from both mental illness and mental wellness fields to take you all the way from anxiety and depression to strength and success. Sometimes we reach a fork in the road and have trouble deciding which way to go. At these times it can be helpful to have someone assist to identify the talents and resources that lie within us, which are sometimes forgotten in the chaos of our daily patterns. When we get back in touch with our inner strengths and resources, we can find our purpose and direction. This is where a positive psychology approach can help.<br>Make contact now with Daniel – your <u>Gold Coast Psychologist</u> – to get your life back on track.</p>
  <a class="btn" style="left:383px;top:405px;width:243px;height:36px">5 Steps Closer To Self Esteem Only $47</a>
</section>
<div class="ph" role="img" aria-label="Photo of a smiling woman in a yellow sweater talking on the phone" style="left:62px;top:3356px;width:430px;height:554px;background:radial-gradient(ellipse at 50% 60%,#f2c53d 0%,#e9d59a 45%,rgba(223,241,246,0) 72%)"></div>

<section class="objectives">
  <h2>Tallowreach has 3 Objectives</h2>
  <div class="obj" style="left:150px"><div class="img" role="img" aria-label="Photo of a thoughtful woman at a laptop" style="background:linear-gradient(160deg,#8b6a57,#3b2a24)"></div><div class="cap">Alleviate distress</div></div>
  <div class="obj" style="left:458px"><div class="img" role="img" aria-label="Photo of a woman stretching her arms by a bright window" style="background:linear-gradient(160deg,#f4f1ea,#c9d8dc)"></div><div class="cap">Take the next step in helping you create a fulfilling, meaningful and enjoyable life through coaching and positive psychology</div></div>
  <div class="obj" style="left:765px"><div class="img" role="img" aria-label="Photo of an older couple sitting on a park bench" style="background:linear-gradient(160deg,#b9bfae,#4f5a43)"></div><div class="cap">Learn, implement and habitualise advanced performance strategies for lasting change.</div></div>
</section>

<div class="footer-rule" style="top:4585px"></div>
<footer>
  <div class="fcol" style="left:150px"><h4>Daniel Hartley</h4><ul>
    <li><svg class="tick"><use href="#tick"/></svg>Registered Psychologist</li>
    <li><svg class="tick"><use href="#tick"/></svg>Society Member</li>
    <li><svg class="tick"><use href="#tick"/></svg>Accredited Life Coach</li>
    <li><svg class="tick"><use href="#tick"/></svg>Trauma Therapy Full Member</li></ul></div>
  <div class="fcol" style="left:395px"><h4>Contact Us</h4><ul>
    <li><svg class="tick"><use href="#tick"/></svg>48 Larkspur Ave, Burleigh</li>
    <li><svg class="tick"><use href="#tick"/></svg>0400 213 987</li>
    <li><svg class="tick"><use href="#tick"/></svg>Fax: (07) 5500 1234</li>
    <li><svg class="tick"><use href="#tick"/></svg>8:00am – 7:00pm (appt. Only)</li></ul></div>
  <div class="fcol" style="left:640px"><h4>Helpful Links</h4><ul>
    <li><svg class="tick"><use href="#tick"/></svg>Home</li>
    <li><svg class="tick"><use href="#tick"/></svg>About Us</li>
    <li><svg class="tick"><use href="#tick"/></svg>Services &amp; Fees</li>
    <li><svg class="tick"><use href="#tick"/></svg>Book Today</li></ul></div>
  <div class="fcol" style="left:885px"><h4>Our Services</h4><ul>
    <li><svg class="tick"><use href="#tick"/></svg>Anxiety and Depression</li>
    <li><svg class="tick"><use href="#tick"/></svg>Anger Management</li>
    <li><svg class="tick"><use href="#tick"/></svg>Dating and Relationships</li>
    <li><svg class="tick"><use href="#tick"/></svg>Self Esteem</li>
    <li><svg class="tick"><use href="#tick"/></svg>Trauma inc. EMDR</li></ul></div>
  <div class="footer-rule" style="top:4932px;background:#d9c9dc"></div>
  <div class="foot-brand"><i></i>TALLOWREACH</div>
  <div class="legal">Privacy Policy &nbsp;–&nbsp; Cookie Policy &nbsp;–&nbsp; Terms and Conditions &nbsp;–&nbsp; Online Course Terms and conditions</div>
  <div class="copy">Copyright © 2024 Tallowreach</div>
</footer>
</body>
</html>
```